Launch of a new Investment fund

Im looking for someone design a logo and website for my Investment fund located in Singapore.

Attached to this project you will find a project scope document that details exactly what i am looking for and also includes a website copy that i have written up. I am happy for you to take your own inspiration as well to design the website. At this stage the website wont be very detailed as there isn't much information to showcase. I will require the website to be easily editable in the future so i can update it with progress the fund makes.

If you require any further details on the project please reach out to me

Coding

Coded - Design and coding required

Number of Pages Required

4 page

```html
<!DOCTYPE html>
<html lang="en">
<head>
<meta charset="utf-8">
<title>Kestrel Capital Management</title>
<link rel="stylesheet" href="https://fonts.googleapis.com/css2?family=Poppins:wght@300;400;500;600;700&display=swap">
<style>
:root{
  --blue:#0a8fd1;
  --ink:#1e1e1e;
  --text:#444;
  --muted:#888;
  --light:#f5f5f5;
  --footer:#2b2b2b;
  --footer-bar:#3a3a3a;
  --white:#fff;
}
*{box-sizing:border-box;margin:0;padding:0}
html,body{width:1200px;height:3831px;overflow:hidden}
body{position:relative;font-family:'Poppins',sans-serif;color:var(--text);background:var(--white)}
.abs{position:absolute}
/* header */
.site-header{left:0;top:0;width:1200px;height:135px;background:var(--white)}
.brand{left:88px;top:40px;display:flex;align-items:center;gap:12px}
.brand-square{width:14px;height:14px;background:var(--blue)}
.brand-name{font-weight:600;font-size:24px;color:var(--ink);letter-spacing:1px;text-transform:uppercase;line-height:1.1}
.main-nav{right:85px;top:60px;display:flex;gap:36px;font-size:14px;color:#333;text-transform:uppercase}
.main-nav .active{color:var(--blue);border-bottom:3px solid var(--blue);padding-bottom:14px}
/* hero */
.hero{left:0;top:135px;width:1200px;height:727px;background:linear-gradient(100deg,#b7b2ab 0%,#8e8780 35%,#6f665d 55%,#9a8f84 75%,#cfc7bc 100%)}
.hero-band{left:0;top:293px}
.hero-title{left:85px;top:330px;font-weight:700;font-size:42px;line-height:52px;color:var(--white);text-transform:uppercase}
.hero-btn{left:88px;top:464px;width:217px;height:72px;background:var(--blue);color:var(--white);font-size:20px;display:flex;align-items:center;justify-content:center;gap:14px}
.hero-dots{left:564px;top:646px;display:flex;gap:5px}
.hero-dots span{width:14px;height:14px;border-radius:50%;background:rgba(255,255,255,.5)}
.hero-dots span:first-child{background:var(--white)}
/* section headings */
.sec-head{display:flex;align-items:center;gap:12px;font-size:40px;font-weight:400;color:var(--ink);text-transform:uppercase;line-height:1}
.sec-head .mark{font-weight:400;font-size:40px;color:var(--ink)}
.sec-head .sq{width:14px;height:14px;background:var(--blue)}
.body-copy{font-size:15.5px;line-height:27.5px;text-align:justify;color:var(--text)}
/* investments */
.investments{left:0;top:1967px;width:1200px;height:717px;background:var(--light)}
.inv-sub{left:0;top:2145px;width:1200px;text-align:center;font-size:15.5px;line-height:28px}
.card{top:2232px;width:243px;height:351px;background:var(--white);box-shadow:0 2px 8px rgba(0,0,0,.08);padding:4px}
.card-img{height:139px}
.card h3{font-size:14.5px;font-weight:600;color:var(--ink);margin:28px 18px 8px;text-transform:uppercase}
.card p{font-size:11.5px;line-height:20.5px;margin:0 18px;text-align:justify;color:#555}
/* contact */
.field{background:var(--white);border:1px solid #e3e3e3;box-shadow:0 2px 6px rgba(0,0,0,.06);font-size:14.5px;color:#999;padding:0 22px;display:flex;align-items:center}
.field.area{align-items:flex-start;padding-top:24px}
.submit{left:583px;top:3237px;width:187px;height:60px;background:var(--ink);color:var(--white);font-size:19px;font-weight:500;display:flex;align-items:center;justify-content:center}
/* footer */
.site-footer{left:0;top:3398px;width:1200px;height:374px;background:var(--footer)}
.foot-bar{left:0;top:3772px;width:1200px;height:59px;background:var(--footer-bar);color:var(--white);font-size:14px;display:flex;align-items:center;justify-content:center}
.foot-brand{left:90px;top:3530px;width:206px;text-align:center;color:var(--white);font-weight:600;font-size:24px;line-height:30px;text-transform:uppercase}
.socials{left:115px;top:3672px;display:flex;gap:8px}
.socials span{width:33px;height:33px;background:var(--blue)}
.foot-head{font-size:19px;font-weight:500;color:var(--blue);text-transform:uppercase}
.foot-head::after{content:"";display:block;width:40px;height:3px;background:var(--white);margin-top:10px}
.links{list-style:none;font-size:15px;color:var(--white)}
.links li{display:flex;align-items:center;gap:20px;height:31px}
.links li::before{content:"";width:9px;height:9px;background:var(--blue)}
.c-item{display:flex;gap:22px;color:var(--white);font-size:14.5px;line-height:19px;align-items:center}
.c-icon{width:29px;height:29px;background:var(--blue);border-radius:4px;display:flex;align-items:center;justify-content:center;flex:none}
.news-text{color:var(--white);font-size:15px;line-height:21px}
.news-input{width:250px;height:37px;background:var(--white)}
.news-btn{width:124px;height:38px;background:var(--blue);color:var(--white);font-size:12.5px;display:flex;align-items:center;justify-content:center;text-transform:uppercase}
</style>
</head>
<body>

<header class="abs site-header">
  <div class="abs brand" style="position:absolute"><span class="brand-square"></span><span class="brand-name">Kestrel<br>Capital Management</span></div>
  <nav class="abs main-nav">
    <span class="active">Home</span><span>What We Do</span><span>Our Team</span><span>Investments ▾</span><span>Contact Us</span>
  </nav>
</header>

<section class="abs hero" role="img" aria-label="Smiling man with glasses working on a laptop at a desk">
  <svg class="abs hero-band" width="820" height="434" viewBox="0 0 820 434"><polygon points="0,0 820,0 560,434 0,434" fill="rgba(40,40,40,.55)"/></svg>
  <h1 class="abs hero-title">Passion for uncovering<br>new opportunities</h1>
  <div class="abs hero-btn">GET STARTED
    <svg width="22" height="14" viewBox="0 0 22 14"><path d="M1 7h18M13 1l6 6-6 6" stroke="#fff" stroke-width="2.5" fill="none"/></svg>
  </div>
  <div class="abs hero-dots"><span></span><span></span><span></span><span></span></div>
</section>

<!-- about -->
<svg class="abs" style="left:0;top:963px" width="520" height="423" viewBox="0 0 520 423">
  <polygon points="0,0 520,0 375,423 0,423" fill="var(--blue)"/>
  <polygon points="0,0 505,0 365,413 0,413" fill="#9a9a9c"/>
</svg>
<div class="abs" role="img" aria-label="Two students working together at a laptop" style="left:0;top:963px;width:505px;height:413px;clip-path:polygon(0 0,100% 0,72% 100%,0 100%);background:linear-gradient(120deg,#d6d4d2,#8a8684 60%,#4b4645)"></div>
<h2 class="abs sec-head" style="left:556px;top:1014px"><span class="sq"></span><span class="mark">Kestrel</span>About Us</h2>
<div class="abs body-copy" style="left:551px;top:1079px;width:562px">
  <p>A beacon of innovative investment where strategic diversification meets meticulous market comprehension. We navigate the complexities of Global Equities, Real Estate, Venture Capital, Private Equity, and Alternative Assets, focusing on uncovering distinctive investment opportunities for our investors.</p>
  <p style="margin-top:27px">At Kestrel, investment is not just a transaction; it's a carefully orchestrated process, mirroring the meticulous management of personal assets. Our ethos is built on a bedrock of expansive market wisdom and proactive strategy formulation, ensuring our portfolio remains both robust and agile.</p>
</div>

<!-- team -->
<h2 class="abs sec-head" style="left:88px;top:1508px"><span class="sq"></span><span class="mark">Kestrel</span>Our Team</h2>
<div class="abs" style="left:87px;top:1561px;font-size:26px;color:var(--blue)">The Architect of Kestrel's Visionary Path</div>
<p class="abs body-copy" style="left:85px;top:1616px;width:563px;line-height:29px;font-size:15.5px">Meet Marcus, the driving force behind Kestrel Capital Management. From co-founding Australia's second-largest renewable energy company to pioneering ventures in diverse sectors, Marcus's entrepreneurial journey is marked by a passion for market innovation and sustainable growth. With over a decade of diverse business scaling experience, Marcus established Kestrel Capital, evolving from personal investment to a trust-fortified endeavour of market innovation and niche investment exploration.</p>
<svg class="abs" style="left:684px;top:1469px" width="516" height="422" viewBox="0 0 516 422">
  <polygon points="155,0 516,0 516,422 0,422" fill="var(--blue)"/>
</svg>
<div class="abs" role="img" aria-label="Team of colleagues gathered around a laptop in a meeting room" style="left:690px;top:1479px;width:510px;height:412px;clip-path:polygon(30% 0,100% 0,100% 100%,0 100%);background:linear-gradient(160deg,#dcd8cf,#9a8f82 50%,#6e5a4c)"></div>

<!-- investments -->
<section class="abs investments"></section>
<h2 class="abs sec-head" style="left:0;top:2078px;width:1200px;justify-content:center"><span class="sq"></span><span class="mark">Kestrel</span>Investments</h2>
<p class="abs inv-sub">Kestrel's portfolio showcases our ability to identify undervalued opportunities with<br>significant growth potential.</p>

<article class="abs card" style="left:88px">
  <div class="card-img" role="img" aria-label="Founders discussing a startup plan at a whiteboard" style="background:linear-gradient(135deg,#c9c4bd,#6e6a66)"></div>
  <h3>Venture Capital</h3>
  <p>Strategic investments in venture capital, where we harness our industry contacts and market understanding to invest in high growth startups and businesses.</p>
</article>
<article class="abs card" style="left:349px">
  <div class="card-img" role="img" aria-label="Calculator and financial charts on a desk" style="background:linear-gradient(135deg,#eceae6,#a9a39a 60%,#c55b4d)"></div>
  <h3>Private Equity</h3>
  <p>Access to investments in cutting edge sectors, featuring companies like Lumen AI, Chatterly, Vireo Media, Datamesh, Orbitra, Synapta, Fieldex, Corvex Systems and Quarry Games</p>
</article>
<article class="abs card" style="left:611px">
  <div class="card-img" role="img" aria-label="Stock market charts on a laptop and phone" style="background:linear-gradient(135deg,#1d2530,#36506b 60%,#2a3b2e)"></div>
  <h3>Global Equity Markets</h3>
  <p>We've demonstrated exceptional skill in identifying undervalued stocks and markets with high growth potential, leveraging in-depth research and market analysis</p>
</article>
<article class="abs card" style="left:872px">
  <div class="card-img" role="img" aria-label="Glass skyscrapers seen from below against a blue sky" style="background:linear-gradient(180deg,#7fb4e3,#3e6f9c 70%,#1d3450)"></div>
  <h3>Property Development</h3>
  <p>Curated development projects, exemplifying our ability to identify and capitalise on high-value real estate opportunities.</p>
</article>

<!-- contact -->
<svg class="abs" style="left:0;top:2797px" width="535" height="489" viewBox="0 0 535 489">
  <polygon points="0,0 535,0 390,489 0,489" fill="var(--blue)"/>
</svg>
<div class="abs" role="img" aria-label="Laptop with trading charts, calculator and magnifying glass on a white desk" style="left:0;top:2797px;width:525px;height:479px;clip-path:polygon(0 0,100% 0,73% 100%,0 100%);background:linear-gradient(135deg,#3a4048,#d9d9d9 45%,#f1f1f1)"></div>
<h2 class="abs sec-head" style="left:582px;top:2803px"><span class="sq"></span><span class="mark">Kestrel</span>Contact Us</h2>
<div class="abs field" style="left:580px;top:2891px;width:256px;height:52px">First Name:</div>
<div class="abs field" style="left:858px;top:2891px;width:254px;height:52px">Last Name:</div>
<div class="abs field" style="left:580px;top:2965px;width:256px;height:52px">Phone:</div>
<div class="abs field" style="left:858px;top:2965px;width:254px;height:52px">Email:</div>
<div class="abs field area" style="left:580px;top:3041px;width:532px;height:164px">Mesage:</div>
<div class="abs submit">SUBMIT</div>

<!-- footer -->
<footer class="abs site-footer"></footer>
<div class="abs foot-brand">
  <div style="width:14px;height:14px;background:var(--blue);margin:0 auto 14px"></div>
  Kestrel<br>Capital Management
</div>
<div class="abs socials"><span></span><span></span><span></span><span></span></div>

<div class="abs" style="left:373px;top:3477px">
  <div class="foot-head">Quick Links</div>
  <ul class="links" style="margin-top:38px">
    <li>Home</li><li>What We Do</li><li>Our Team</li><li>Investments</li><li>Contact Us</li>
  </ul>
</div>

<div class="abs" style="left:569px;top:3477px">
  <div class="foot-head">Contact Us</div>
  <div style="margin-top:40px;display:flex;flex-direction:column;gap:25px">
    <div class="c-item"><span class="c-icon"><svg width="15" height="15" viewBox="0 0 24 24"><path d="M6.6 10.8a15 15 0 006.6 6.6l2.2-2.2a1 1 0 011-.25 11.4 11.4 0 003.6.6 1 1 0 011 1V20a1 1 0 01-1 1A17 17 0 013 4a1 1 0 011-1h3.5a1 1 0 011 1 11.4 11.4 0 00.6 3.6 1 1 0 01-.25 1z" fill="#fff"/></svg></span><span>CALL US<br>8000 123 4567</span></div>
    <div class="c-item"><span class="c-icon"><svg width="15" height="12" viewBox="0 0 24 18"><rect x="1" y="1" width="22" height="16" fill="#fff"/><path d="M1 1l11 9 11-9" stroke="#0a8fd1" stroke-width="2" fill="none"/></svg></span><span>EMAIL US<br>hello@kestrelcapital.example</span></div>
    <div class="c-item"><span class="c-icon"><svg width="12" height="16" viewBox="0 0 24 32"><path d="M12 0a11 11 0 00-11 11c0 8 11 21 11 21s11-13 11-21A11 11 0 0012 0zm0 15a4 4 0 110-8 4 4 0 010 8z" fill="#fff"/></svg></span><span>Address line Dummy Here<br>Address line Here</span></div>
  </div>
</div>

<div class="abs" style="left:865px;top:3475px">
  <div class="foot-head">Our Newsletter</div>
  <p class="news-text" style="margin-top:38px">Subscribe our newsletter to get<br>the latest news.</p>
  <div class="news-input" style="margin-top:17px"></div>
  <div class="news-btn" style="margin-top:12px">Subscribe</div>
</div>

<div class="abs foot-bar">Copyright © 2023 All Rights Reserved By Kestrel Capital Management</div>

</body>
</html>
```